Flyer for an pediatric sleep consultancy - to distribute to play and childcare centers etc.

I need a flyer that will attract the attention of parents with children between the age of babies to toddlers, who may be experiencing sleep issues. The flyer will be placed at places such as community centers, doctors room, play centers, kindergardens, etc.

My company is called "The Quiet Meadow Studio" and provides a sleep consultancy service. My service essentially provides a customized plan for parents to follow and general advice and guidance. It is not medical advice.

I like to the flyer to have an overall tone that is soft and peaceful with a clean and beautiful design, however can catch the attention of parents who may be struggling with their child's sleep issues and are sleep deprived. I would like photos with minimal text. The colour I use is a brownish rose. I will attach some of my designs to give you an idea. You can have a look at my homepage as well to get an idea about my esthetic direction and the colour. Although the colour of my page is a bit too brownish....

I will provide the text to appear in the flyer once I have a better idea of the layout that I prefer for the flyer. The text however wont be extensive, just some catchy points.

I want to direct people to my website which is www.quietmeadowstudio-example.com
I offer a first FREE evaluation call, to the parents, to get to know each other better, learn about their child's particular sleep problems and see if we are a good fit and can work together. I would like to have this information somehow on the flyer, so that the parents will contact me.
I also have a facebook page, which is: The Quiet Meadow Studio

I have a logo that I would like to appear on the flyer. I will attach the file once the uploader on art bazaar is fixed.

When I print the flyer - I like to print A5 SIZE ... please make sure the formatting is OK for this size.

Here are some text ideas. of course all of it would be too much, I guess. On the front of the flyer I would like to have some catchy phrase or something similar to get people interested and to want to know more. On the back there could be a bit more text and information. But I'm open too suggestions....
I'm not too sure about the wording yet. But here are some text that I might be use:

Is sleep an issue in your home?

Is your baby having trouble sleeping? ... are you?!
I can help!

Sleep, baby, sleep….

Teaching children how to sleep

The Quiet Meadow Studio is a pediatric sleep consultancy that specializes in helping parents with children who struggle to develop good and healthy sleep habits.
Disruptive sleep patterns or not enough sleep can affect the physical, mental and emotional development of your child.

Of course nobody plans to have a sleep problem, but habits can become easily ingrained and spiral quickly out of control and you can find yourself sleep deprived, desperate and not too sure what to do. You see all the other sleeping babies and wish there was someone who understood what you were going through?! Well, there is!

Contact me for a free 15 minute consultation.

This 15 minute „mini“ consultation is a chance to discuss your unique sleep challenges and sleep goals with me. I will provide you with an overview of how I will work with your family to achieve your wildest sleep dreams (goals).
Furthermore do I understand and believe that every child and their family is unique and there is no one size fits all!
I would love to have a chat with you and talk about how I can help make things easier for you and your family!

Do I need a sleep consultant for my child?
The answer is yes if:
- if your child will only fall asleep when nursing or bottle feeding
- if your child needs a dummy or other external aid, like being rocked, patted or taken for a care ride to fall asleep
- if your good night routine is a challenging and exhausting procedure instead of a relaxed and enjoyable moment for the whole family
- if sleep is a constant battle in your home which leaves you feeling frustrated and exhausted
- if your own lack of sleep is taking a toll on you and the whole family

What can I do for you?

I will:

- Guide you to set an age appropriate foundation for good sleep
- Create an individual sleep plan tailored especially to your child’s sleep needs and circumstances
- Help you to teach your childto go to sleep and get back to sleep independently during the night
- show you how to teach your child to take healthful, restorative naps
-Learn

Contact:

Marta Lindqvist
info@quietmeadowstudio-example.com
www.quietmeadowstudio-example.com
+34 612 380 574

Consultations in English, German or Spanish via Phone/CallNest or home consultation

Reason: I have to go on a business trip and won't be able to choose a design until the deadline. During the trip I won't have time to give feedback and ask for changes. thank you

Target Market(s)

parents, sleep deprived mothers, young families, child care provider,

Industry/Entity Type

Baby Care

Contact Information for Business Card

Marta Lindqvist
pediatric sleep consultant
+34 612 380 574

```html
<!DOCTYPE html>
<html lang="en">
<head>
<meta charset="utf-8">
<title>The Quiet Meadow Studio – Flyer</title>
<link rel="stylesheet" href="https://fonts.googleapis.com/css2?family=Crimson+Text:wght@400;600;700&family=Open+Sans:wght@400;600;700&family=Roboto+Condensed:wght@400;700&display=swap">
<style>
  :root {
    --rose: #e5877a;
    --rose-deep: #d9705f;
    --rose-soft: #f2c3b9;
    --rose-pale: #fbe9e4;
    --ink: #222222;
    --grey-text: #777777;
    --paper: #ffffff;
    --backdrop: #e6e3e1;
    --serif: "Crimson Text", Georgia, serif;
    --sans: "Open Sans", Arial, sans-serif;
    --condensed: "Roboto Condensed", Arial, sans-serif;
  }
  * { box-sizing: border-box; margin: 0; padding: 0; }
  html, body { width: 1200px; height: 900px; overflow: hidden; }
  body { background: var(--backdrop); position: relative; font-family: var(--sans); color: var(--ink); }

  .page { position: absolute; top: 60px; width: 554px; height: 785px; background: var(--paper); overflow: hidden; box-shadow: 0 2px 10px rgba(0,0,0,.18); }
  .page--front { left: 30px; }
  .page--back { left: 614px; }
  .abs { position: absolute; }
  .shapes { position: absolute; inset: 0; width: 100%; height: 100%; }

  /* ---------- front ---------- */
  .photo-fill { position: absolute; }
  .front-hero-photo { left: -10px; top: -40px; width: 300px; height: 345px; border-radius: 50%; background: radial-gradient(circle at 45% 55%, #f1e6e2 0%, #e2d6d2 55%, #cfc4c1 100%); }
  .brand-name { font-family: var(--sans); font-weight: 400; color: var(--rose-deep); font-size: 14px; white-space: nowrap; }
  .front-brand { left: 318px; top: 34px; width: 190px; text-align: center; }
  .brand-dot { display: block; width: 30px; height: 30px; border-radius: 50%; background: var(--rose-soft); margin: 0 auto 8px; }
  .headline { left: 308px; top: 122px; width: 210px; text-align: center; font-family: var(--serif); font-weight: 700; color: var(--rose-deep); font-size: 22px; line-height: 24px; }
  .subhead { left: 298px; top: 174px; width: 230px; text-align: center; font-family: var(--serif); color: var(--grey-text); font-size: 22px; line-height: 24px; }
  .lullaby { left: 298px; top: 250px; width: 230px; text-align: center; font-family: var(--sans); font-weight: 600; color: var(--rose-deep); font-size: 19px; letter-spacing: .3px; }

  .offer-box { left: 325px; top: 295px; width: 193px; height: 325px; background: var(--rose); box-shadow: 2px 3px 6px rgba(0,0,0,.2); padding: 10px 12px; color: #fff; }
  .offer-title { font-family: var(--sans); font-weight: 600; font-size: 16px; line-height: 20px; text-align: center; margin: 0 6px 12px; }
  .offer-text { font-size: 11px; line-height: 13.2px; text-align: justify; }

  .intro { left: 40px; top: 363px; width: 266px; }
  .intro-title { font-family: var(--serif); font-weight: 600; color: var(--rose-deep); font-size: 19px; margin-bottom: 6px; }
  .intro p { font-size: 11.2px; line-height: 13.4px; text-align: justify; margin-bottom: 12px; }

  .front-photo-a { left: 24px; top: 615px; width: 140px; height: 140px; border-radius: 50%; background: radial-gradient(circle at 50% 45%, #f6e2d8 0%, #e9cbbd 60%, #d8b3a3 100%); }
  .front-photo-b { left: 175px; top: 650px; width: 120px; height: 120px; border-radius: 50%; background: radial-gradient(circle at 50% 50%, #f4e6e1 0%, #e5d3cd 70%, #d6c1ba 100%); }

  .contact { left: 311px; top: 633px; width: 230px; }
  .contact-label { font-size: 12.5px; font-weight: 700; }
  .contact-name { font-family: var(--condensed); font-weight: 700; color: var(--rose); font-size: 19px; }
  .contact-phone { font-family: var(--condensed); font-weight: 700; font-size: 20px; margin-top: 1px; }
  .contact-line { font-size: 11.2px; line-height: 15px; display: flex; align-items: center; gap: 5px; }
  .contact-line svg { flex: none; }

  /* ---------- back ---------- */
  .back-hero-photo { left: 0; top: 0; width: 554px; height: 785px; background: linear-gradient(180deg, #eceef0 0%, #f3f3f4 30%, #f7f7f7 45%, #fbfbfb 70%, #ffffff 100%); }
  .section-bar { background: var(--rose); color: #fff; font-family: var(--serif); font-weight: 700; font-size: 18px; line-height: 24px; padding: 0 8px; white-space: nowrap; }
  .bar-need { left: 23px; top: 242px; }
  .bar-offer { left: 23px; top: 440px; }
  .list-lead { font-size: 12.5px; font-weight: 700; }
  .lead-yes { left: 32px; top: 274px; }
  .lead-will { left: 36px; top: 470px; }
  .checklist { list-style: none; font-size: 12px; line-height: 16px; }
  .checklist li { position: relative; padding-left: 17px; margin-bottom: 2.5px; }
  .checklist li::before { content: ""; position: absolute; left: 0; top: 2px; width: 10px; height: 10px; border: 1px solid var(--rose-deep); background: #fff; }
  .checklist li::after { content: ""; position: absolute; left: 3px; top: 3px; width: 4px; height: 7px; border-right: 2px solid var(--rose-deep); border-bottom: 2px solid var(--rose-deep); transform: rotate(40deg); }
  .list-yes { left: 32px; top: 294px; width: 470px; }
  .list-will { left: 36px; top: 489px; width: 400px; }
  .list-will li { max-width: 400px; }

  .back-hand-photo { left: 400px; top: 450px; width: 154px; height: 230px; background: linear-gradient(160deg, #fff 0%, #f6e7e1 45%, #eed7ce 100%); border-radius: 60px 0 0 40px; }
  .back-brand { left: 28px; top: 632px; width: 170px; text-align: center; }
  .info-circle { left: 222px; top: 614px; width: 130px; height: 130px; border-radius: 50%; background: var(--rose); border: 4px solid #fff; box-shadow: 0 0 0 2px var(--rose-soft); color: #fff; font-size: 10.5px; font-weight: 700; line-height: 13.4px; text-align: center; display: flex; align-items: center; justify-content: center; padding: 12px; }
  .back-photo-small { left: 348px; top: 622px; width: 90px; height: 90px; border-radius: 50%; border: 3px solid #fff; background: radial-gradient(circle at 50% 50%, #eef0f3 0%, #dcdde2 70%, #c9c9d0 100%); }
  .back-contact { left: 355px; top: 713px; width: 180px; text-align: center; color: #fff; }
  .back-contact .name { font-family: var(--condensed); font-weight: 700; font-size: 16px; }
  .back-contact .phone { font-family: var(--condensed); font-weight: 700; font-size: 21px; line-height: 22px; }
  .back-footer { left: 0; top: 757px; width: 554px; text-align: center; color: #fff; font-size: 12px; display: flex; justify-content: center; align-items: center; gap: 6px; }
</style>
</head>
<body>

<section class="page page--front">
  <div class="photo-fill front-hero-photo" role="img" aria-label="Photo of a newborn asleep in a white crib"></div>
  <svg class="shapes" viewBox="0 0 554 785" aria-hidden="true">
    <path d="M0 300 C 70 330, 180 330, 260 305" fill="none" stroke="var(--rose)" stroke-width="7"/>
    <path d="M260 305 C 300 270, 320 200, 300 120 C 285 60, 250 20, 200 0" fill="none" stroke="var(--rose)" stroke-width="7"/>
    <path d="M230 318 C 300 300, 380 295, 554 310 L 554 340 C 450 318, 350 312, 230 318 Z" fill="var(--rose-soft)"/>
    <path d="M0 718 C 80 790, 220 770, 300 720 L 300 785 L 0 785 Z" fill="var(--rose)"/>
    <path d="M250 745 C 350 720, 450 740, 554 730 L 554 785 L 250 785 Z" fill="var(--rose-pale)"/>
  </svg>

  <div class="abs front-brand"><span class="brand-dot"></span><span class="brand-name">The Quiet Meadow Studio</span></div>
  <h1 class="abs headline">IS SLEEP AN ISSUE IN YOUR HOME?</h1>
  <p class="abs subhead">Is your baby having trouble sleeping?<br>... are you?! I can help!</p>
  <p class="abs lullaby">Sleep, baby, sleep….</p>

  <div class="abs offer-box">
    <h2 class="offer-title">Contact me for a free 15 minute consultation.</h2>
    <p class="offer-text">This 15 minute „mini“ consultation is a chance to discuss your unique sleep challenges and sleep goals with me. I will provide you with an overview of how I will work with your family to achieve your wildest sleep dreams (goals). Furthermore do I understand and believe that every child and their family is unique and there is no one size fits all! I would love to have a chat with you and talk about how I can help make things easier for you and your family!</p>
  </div>

  <div class="abs intro">
    <h2 class="intro-title">Teaching children how to sleep</h2>
    <p>The Quiet Meadow Studio is a pediatric sleep consultancy that specializes in helping parents with children who struggle to develop good and healthy sleep habits. Disruptive sleep patterns or not enough sleep can affect the physical, mental and emotional development of your child.</p>
    <p>Of course nobody plans to have a sleep problem, but habits can become easily ingrained and spiral quickly out of control and you can find yourself sleep deprived, desperate and not too sure what to do. You see all the other sleeping babies and wish there was someone who understood what you were going through?! Well, there is!</p>
  </div>

  <div class="photo-fill front-photo-a" role="img" aria-label="Photo of a mother and baby sleeping together"></div>
  <div class="photo-fill front-photo-b" role="img" aria-label="Photo of a toddler sleeping on a pillow"></div>

  <div class="abs contact">
    <p><span class="contact-label">Contact: </span><span class="contact-name">Marta Lindqvist</span></p>
    <p class="contact-phone">+34 612 380 574</p>
    <p class="contact-line"><svg width="10" height="8" viewBox="0 0 10 8"><rect x=".5" y=".5" width="9" height="7" fill="none" stroke="var(--rose)"/><path d="M.5 .5 L5 4.5 L9.5 .5" fill="none" stroke="var(--rose)"/></svg>info@quietmeadowstudio-example.com</p>
    <p class="contact-line"><svg width="10" height="10" viewBox="0 0 10 10"><circle cx="5" cy="5" r="4.5" fill="var(--rose)"/></svg>www.quietmeadowstudio-example.com</p>
  </div>
</section>

<section class="page page--back">
  <div class="photo-fill back-hero-photo" role="img" aria-label="Photo of a toddler peeking over white bedding"></div>
  <div class="photo-fill back-hand-photo" role="img" aria-label="Photo of a parent's hand holding a baby's hand"></div>
  <svg class="shapes" viewBox="0 0 554 785" aria-hidden="true">
    <path d="M0 690 C 120 740, 300 700, 554 650 L 554 785 L 0 785 Z" fill="var(--rose-pale)"/>
    <path d="M0 725 C 150 760, 350 720, 554 690 L 554 785 L 0 785 Z" fill="var(--rose)"/>
  </svg>

  <h2 class="abs section-bar bar-need">Do I need a sleep consultant for my child?</h2>
  <p class="abs list-lead lead-yes">The answer is yes if:</p>
  <ul class="abs checklist list-yes">
    <li>if your child will only fall asleep when nursing or bottle feeding</li>
    <li>if your child needs a dummy or other external aid, like being rocked, patted<br>or taken for a care ride to fall asleep</li>
    <li>if your good night routine is a challenging and exhausting procedure instead<br>of a relaxed and enjoyable moment for the whole family</li>
    <li>if sleep is a constant battle in your home which leaves you feeling frustrated<br>and exhausted</li>
    <li>if your own lack of sleep is taking a toll on you and the whole family</li>
  </ul>

  <h2 class="abs section-bar bar-offer">What can I do for you?</h2>
  <p class="abs list-lead lead-will">I will :</p>
  <ul class="abs checklist list-will">
    <li>Guide you to set an age appropriate foundation for good sleep</li>
    <li>Create an individual sleep plan tailored especially to your<br>child’s sleep needs and circumstances</li>
    <li>Help you to teach your childto go to sleep and get back<br>to sleep independently during the night</li>
    <li>show you how to teach your child to take healthful, restorative naps</li>
    <li>Learn</li>
  </ul>

  <div class="abs back-brand"><span class="brand-dot"></span><span class="brand-name">The Quiet Meadow Studio</span></div>
  <div class="abs info-circle">Consultations in English, German or Spanish via Phone/CallNest or home consultation</div>
  <div class="photo-fill back-photo-small" role="img" aria-label="Photo of a baby standing in a crib"></div>

  <div class="abs back-contact">
    <p class="name">Marta Lindqvist</p>
    <p class="phone">+34 612 380 574</p>
  </div>
  <p class="abs back-footer">
    <svg width="12" height="9" viewBox="0 0 12 9" aria-hidden="true"><rect x=".5" y=".5" width="11" height="8" fill="none" stroke="#fff"/><path d="M.5 .5 L6 5 L11.5 .5" fill="none" stroke="#fff"/></svg>
    info@quietmeadowstudio-example.com &nbsp;|&nbsp;
    <svg width="11" height="11" viewBox="0 0 11 11" aria-hidden="true"><circle cx="5.5" cy="5.5" r="5" fill="#fff"/></svg>
    www.quietmeadowstudio-example.com
  </p>
</section>

</body>
</html>
```